Modular Cat Home Business Card

We need a business card for a modular and configurable cat playhouse, known as NookBox. NookBoxes can be integrated with human furniture. They come in cubes that are stackable, customizable and interchangeable.

Our name card should be in the shape of an isometric cube (not a normal business card size) with the NookBox logo inside the cube on one side of the namecard. If a home can be created inside the cube to show a homely environment, that could be an option. We are toying with the idea of having the cube side black and white and the flip side with our details, colorful. Our brand colours are pastel. They include pastel yellow, pink, purple, blue and orange. On the flip side, should be details including our name, position, email address, website, contact number.

The overall design should be clean, minimalistic, yet portray fun, happiness and quirky style. The product is design oriented so the name card should reflect likewise.

Target Market(s)

Cat Owners, Home owners, Mid 20s

Industry/Entity Type

Business

Contact Information for Business Card

Name, position, company name, phone number, email address, website. Name font should be bigger.

Colors
f8ba93
f9d9e8
ecdaeb
cee9f5
cfeae6
eaf2ce
fcf9cd
fce8d3
fbd4d5

Requirements
Must have
• The logo
• A variety of pastel colors
• A die cut in the form of a cube
Nice to have
• A home in the cube, to show furniture integration

```html
<!DOCTYPE html>
<html lang="en">
<head>
<meta charset="utf-8">
<title>NookBox Business Card</title>
<link href="https://fonts.googleapis.com/css2?family=Open+Sans:wght@300;400&display=swap" rel="stylesheet">
<style>
  :root {
    --backdrop: #262626;
    --card-dark: #7b7b7b;
    --card-dark-edge: #939393;
    --ink-light: #f2f2f2;
    --ink-dark: #6a6f74;
    --ink-soft: #8b8f99;
    --fold-line: rgba(255,255,255,0.35);
    --pastel-orange: #f8ba93;
    --pastel-pink: #f9d9e8;
    --pastel-purple: #ecdaeb;
    --pastel-blue: #cee9f5;
    --pastel-mint: #cfeae6;
    --pastel-lime: #eaf2ce;
    --pastel-yellow: #fcf9cd;
    --pastel-peach: #fce8d3;
    --pastel-rose: #fbd4d5;
  }
  * { margin: 0; padding: 0; box-sizing: border-box; }
  html, body { width: 1200px; height: 1015px; overflow: hidden; }
  body {
    background: var(--backdrop);
    font-family: "Open Sans", sans-serif;
    font-weight: 300;
    position: relative;
  }
  .card {
    position: absolute;
    left: 120px;
    width: 960px;
    height: 420px;
  }
  .card--back { top: 50px; }
  .card--front { top: 540px; }
  .card-shape { position: absolute; inset: 0; width: 960px; height: 420px; }
  .card--front .card-shape { transform: scaleX(-1); }

  .brand {
    position: absolute;
    display: flex;
    align-items: center;
    gap: 12px;
  }
  .brand-square {
    width: 30px; height: 30px;
    border: 2px solid currentColor;
  }
  .brand-name { font-size: 30px; font-weight: 300; letter-spacing: 0.5px; }
  .brand-tag {
    position: absolute;
    font-size: 13px;
    letter-spacing: 7px;
  }

  .card--back { color: var(--ink-light); }
  .card--back .brand { left: 720px; top: 140px; }
  .card--back .brand-tag { left: 766px; top: 190px; }
  .card--back .site { position: absolute; right: 36px; top: 272px; font-size: 14px; font-weight: 400; }

  .card--front { color: var(--ink-dark); }
  .card--front .brand { left: 360px; top: 130px; }
  .card--front .brand-square { background: var(--pastel-yellow); border-color: var(--ink-dark); }
  .card--front .brand-tag { left: 406px; top: 180px; color: var(--ink-soft); }
  .paw-mark {
    position: absolute; left: 40px; top: 128px;
    width: 64px; height: 64px; border-radius: 50%;
    background: radial-gradient(circle, var(--pastel-orange), var(--pastel-rose));
  }
  .person { position: absolute; left: 118px; top: 132px; }
  .person-name { font-size: 28px; color: var(--ink-soft); line-height: 1.1; }
  .person-title { font-size: 14px; color: var(--ink-soft); margin-top: 2px; }
  .contacts {
    position: absolute; left: 40px; top: 226px;
    list-style: none; display: flex; gap: 24px;
    font-size: 14px; font-weight: 400;
  }
  .contacts li { display: flex; align-items: center; gap: 7px; }
  .contacts svg { width: 14px; height: 14px; }
  .icon-mail path { fill: none; stroke: #e59a6c; stroke-width: 1.5; }
  .icon-phone path { fill: #c38fc0; }
  .icon-web * { fill: none; stroke: #7fb6cf; }
</style>
</head>
<body>

<section class="card card--back">
  <svg class="card-shape" viewBox="0 0 960 420" aria-hidden="true">
    <path d="M220 20 L385 115 L945 115 L945 305 L385 305 L220 400 L55 305 L55 115 Z" fill="var(--card-dark)" stroke="var(--card-dark-edge)" stroke-width="1.5"/>
    <polygon points="220,37.9 355.3,115 220,192.1 84.7,115" fill="var(--backdrop)"/>
    <polygon points="205.15,218.55 205.15,374.35 69.85,296.45 69.85,140.65" fill="var(--backdrop)"/>
    <path d="M220 210 L385 115 M220 210 L220 400" stroke="var(--fold-line)" stroke-width="1" fill="none"/>
  </svg>
  <div class="brand"><span class="brand-square"></span><span class="brand-name">NookBox</span></div>
  <div class="brand-tag">NOOKBOX</div>
  <div class="site">www.nookbox.com</div>
</section>

<section class="card card--front">
  <svg class="card-shape" viewBox="0 0 960 420" aria-hidden="true">
    <defs>
      <linearGradient id="front-wash" x1="0" y1="0" x2="1" y2="0">
        <stop offset="0" stop-color="#fce8d3"/>
        <stop offset="0.35" stop-color="#cfeae6"/>
        <stop offset="1" stop-color="#cee9f5"/>
      </linearGradient>
    </defs>
    <path d="M220 20 L385 115 L945 115 L945 305 L385 305 L220 400 L55 305 L55 115 Z" fill="url(#front-wash)" stroke="#f4f8fa" stroke-width="1.5"/>
    <polygon points="220,20 385,115 220,210 55,115" fill="var(--pastel-yellow)"/>
    <polygon points="55,115 220,210 220,400 55,305" fill="var(--pastel-purple)"/>
    <polygon points="220,210 385,115 385,305 220,400" fill="var(--pastel-rose)"/>
    <polygon points="220,37.9 355.3,115 220,192.1 84.7,115" fill="var(--backdrop)"/>
    <polygon points="205.15,218.55 205.15,374.35 69.85,296.45 69.85,140.65" fill="var(--backdrop)"/>
    <path d="M220 210 L385 115 M220 210 L220 400" stroke="#c4ccd0" stroke-width="1" fill="none"/>
    <rect x="385" y="289" width="62" height="16" fill="#f8ba93"/>
    <rect x="447" y="289" width="62" height="16" fill="#f9d9e8"/>
    <rect x="509" y="289" width="62" height="16" fill="#ecdaeb"/>
    <rect x="571" y="289" width="62" height="16" fill="#cee9f5"/>
    <rect x="633" y="289" width="62" height="16" fill="#cfeae6"/>
    <rect x="695" y="289" width="62" height="16" fill="#eaf2ce"/>
    <rect x="757" y="289" width="62" height="16" fill="#fcf9cd"/>
    <rect x="819" y="289" width="63" height="16" fill="#fce8d3"/>
    <rect x="882" y="289" width="63" height="16" fill="#fbd4d5"/>
  </svg>
  <div class="paw-mark" role="img" aria-label="Paw print decoration"></div>
  <div class="person">
    <div class="person-name">Your Name</div>
    <div class="person-title">Job title</div>
  </div>
  <div class="brand"><span class="brand-square"></span><span class="brand-name">NookBox</span></div>
  <div class="brand-tag">NOOKBOX</div>
  <ul class="contacts">
    <li><svg class="icon-mail" viewBox="0 0 16 16"><path d="M1 3h14v10H1z M2 4l6 5 6-5"/></svg>youremail@example.com</li>
    <li><svg class="icon-phone" viewBox="0 0 16 16"><path d="M4 1l3 3-2 2c1 2 3 4 5 5l2-2 3 3-2 3C7 15 1 9 1 3z"/></svg>000 000 0000</li>
    <li><svg class="icon-web" viewBox="0 0 16 16"><circle cx="8" cy="8" r="6.5" stroke-width="1.3"/><path d="M1.5 8h13M8 1.5c-3 3-3 10 0 13M8 1.5c3 3 3 10 0 13" stroke-width="1"/></svg>nookbox.com</li>
  </ul>
</section>

</body>
</html>
```